Bref créative
Business Cards - Skyline Assessors
Two sided business cards
Simple
Corwin Hask
Certified Appraiser
48270 Millbrook Lane #1174
Ashvale, MD 20391
corwin@plumvexa.com
www.plumvexa.com
Just the logo, either include the text or not (what ever looks better)
Colors and Fonts Guide

```html
<!DOCTYPE html>
<html lang="en">
<head>
<meta charset="utf-8">
<title>Skyline Assessors — Business Cards</title>
<link rel="stylesheet" href="https://fonts.googleapis.com/css2?family=Josefin+Sans:wght@400;600&family=Open+Sans:wght@400;600&display=swap">
<style>
  :root {
    --bg: #e9e6e1;
    --card-white: #ffffff;
    --card-white-edge: #e4e6ea;
    --blue-light: #2f7fc4;
    --blue-dark: #0c3a6b;
    --red-light: #e0252f;
    --red-dark: #b7121c;
    --brand-red: #c3202a;
    --ink: #555a60;
    --ink-soft: #8a8f96;
    --white: #ffffff;
    --sky: #3a8fd6;
  }
  * { box-sizing: border-box; margin: 0; padding: 0; }
  html, body { width: 1200px; height: 828px; overflow: hidden; }
  body {
    background: var(--bg);
    font-family: "Open Sans", Arial, sans-serif;
    position: relative;
  }
  .card {
    position: absolute;
    width: 500px;
    height: 290px;
    border-radius: 14px;
    box-shadow: 0 6px 18px rgba(0,0,0,0.18);
    overflow: hidden;
  }
  .card--info  { left: 70px;  top: 85px;  background: linear-gradient(160deg, var(--card-white), var(--card-white-edge)); }
  .card--blue  { left: 630px; top: 85px;  background: radial-gradient(ellipse at 50% 40%, var(--blue-light), var(--blue-dark)); }
  .card--white { left: 70px;  top: 453px; background: linear-gradient(160deg, var(--card-white), var(--card-white-edge)); }
  .card--red   { left: 630px; top: 453px; background: radial-gradient(ellipse at 50% 40%, var(--red-light), var(--red-dark)); }

  .brand {
    position: absolute;
    left: 0; right: 0;
    display: flex;
    flex-direction: column;
    align-items: center;
    gap: 10px;
  }
  .brand__dot { width: 22px; height: 22px; border-radius: 50%; background: var(--sky); }
  .brand__name {
    font-family: "Josefin Sans", Arial, sans-serif;
    font-weight: 600;
    font-size: 30px;
    letter-spacing: 3px;
    text-transform: uppercase;
    white-space: nowrap;
    color: var(--brand-red);
  }
  .card--blue .brand__name, .card--red .brand__name { color: var(--white); }
  .card--blue .brand__dot, .card--red .brand__dot { background: var(--white); }
  .card--info .brand { top: 30px; gap: 8px; }
  .card--info .brand__dot { width: 18px; height: 18px; }
  .card--info .brand__name { font-size: 24px; }
  .card--blue .brand, .card--white .brand, .card--red .brand { top: 78px; }

  .web {
    position: absolute;
    bottom: 30px; left: 0; right: 0;
    text-align: center;
    font-size: 14px;
    letter-spacing: 2px;
    color: var(--white);
  }
  .card--white .web { color: var(--brand-red); }

  .contact { position: absolute; left: 32px; top: 128px; color: var(--ink); }
  .contact__name { font-weight: 600; font-size: 17px; color: var(--brand-red); }
  .contact__title { font-size: 12px; color: var(--ink-soft); margin-bottom: 12px; }
  .contact__line { font-size: 11px; line-height: 1.6; }
  .contact__label { color: var(--brand-red); display: inline-block; width: 40px; }
</style>
</head>
<body>
  <section class="card card--info">
    <div class="brand">
      <span class="brand__dot"></span>
      <span class="brand__name">Skyline Assessors</span>
    </div>
    <div class="contact">
      <p class="contact__name">Corwin Hask</p>
      <p class="contact__title">Certified Appraiser</p>
      <p class="contact__line">48270 Millbrook Lane #1174, Ashvale, MD 20391</p>
      <p class="contact__line"><span class="contact__label">Cell:</span>555 482 0148</p>
      <p class="contact__line"><span class="contact__label">Email:</span>corwin@plumvexa.com</p>
      <p class="contact__line"><span class="contact__label">Web:</span>www.plumvexa.com</p>
    </div>
  </section>

  <section class="card card--blue">
    <div class="brand">
      <span class="brand__dot"></span>
      <span class="brand__name">Skyline Assessors</span>
    </div>
    <p class="web">www.plumvexa.com</p>
  </section>

  <section class="card card--white">
    <div class="brand">
      <span class="brand__dot"></span>
      <span class="brand__name">Skyline Assessors</span>
    </div>
    <p class="web">www.plumvexa.com</p>
  </section>

  <section class="card card--red">
    <div class="brand">
      <span class="brand__dot"></span>
      <span class="brand__name">Skyline Assessors</span>
    </div>
    <p class="web">www.plumvexa.com</p>
  </section>
</body>
</html>
```